Stationary KV Relay
business card, letterhead, envelopes, email signature,memo pad and invoice/quotes
Project: Stationary KV Relay
Stationary KV Relay   - Telecommunications
Creative Brief
Use same font as used in my logo
or any
Bright & Fun-filled
Tom Variscoff
CEO
3F B28 GALERI NUSAPARK JAKARTA PUSAT 14071
tom@kvrelay.com
www.kvrelay.com
Feel free to utilize different styles but try to stick to the company logo colors as best as possible.
Require: Business card, Stationary, Envelopes, Invoice, E-mail signature & Notepad
pwarnet pwarnet
EPS format upload already
brightoak brightoak
definitely!! but there is lots of designs please rate my design so i will easy to make the stationary of your like designs thanks :)
Business card, Stationary, Envelopes, Invoice, E-mail signature & Notepad
Check your private massage! thanks!
nice for this time

```html
<!DOCTYPE html>
<html lang="en">
<head>
<meta charset="utf-8">
<title>KV Relay — Business Card</title>
<link href="https://fonts.googleapis.com/css2?family=Michroma&display=swap" rel="stylesheet">
<style>
  :root {
    --bg: #d9dadb;
    --card: #ffffff;
    --blue: #1556a8;
    --blue-deep: #0d3f86;
    --orange: #f5a21c;
    --text-grey: #6d6f73;
    --shadow: rgba(0, 0, 0, 0.18);
  }
  * { margin: 0; padding: 0; box-sizing: border-box; }
  html, body {
    width: 1200px; height: 984px; overflow: hidden;
    background: var(--bg);
    font-family: "Michroma", sans-serif;
  }
  .stage { position: relative; width: 1200px; height: 984px; }
  .card {
    position: absolute; left: 240px;
    width: 720px; height: 411px;
    background: var(--card);
    border-radius: 22px;
    overflow: hidden;
    box-shadow: 0 10px 26px var(--shadow);
  }
  .card--back { top: 52px; }
  .card--front { top: 521px; }

  .brand { display: flex; align-items: center; gap: 14px; }
  .brand__dot {
    width: 46px; height: 46px; border-radius: 50%;
    background: var(--orange);
  }
  .brand__name {
    font-size: 30px; color: var(--blue); letter-spacing: 1px; white-space: nowrap;
  }

  .card--back .brand {
    position: absolute; left: 50%; top: 150px; transform: translateX(-50%);
  }
  .card--back .web {
    position: absolute; left: 0; right: 0; top: 232px;
    text-align: center; font-size: 11px; letter-spacing: 7px; color: var(--text-grey);
  }

  .swoosh { position: absolute; left: 0; top: 0; width: 720px; height: 411px; }
  .card--front .brand { position: absolute; left: 190px; top: 52px; }
  .holder { position: absolute; left: 262px; top: 150px; }
  .holder__name { font-size: 13px; color: var(--blue); letter-spacing: 0.5px; }
  .holder__role { font-size: 9px; color: var(--text-grey); margin-top: 6px; }

  .contact {
    position: absolute; left: 430px; top: 248px; list-style: none;
  }
  .contact li {
    display: flex; align-items: flex-start; gap: 9px;
    font-size: 9px; color: var(--text-grey); line-height: 1.45; margin-bottom: 5px;
  }
  .contact svg { flex: none; width: 14px; height: 14px; margin-top: 1px; }
</style>
</head>
<body>
<main class="stage">

  <section class="card card--back" aria-label="Business card back">
    <div class="brand">
      <span class="brand__dot"></span>
      <span class="brand__name">KV Relay</span>
    </div>
    <p class="web">www.kvrelay.com</p>
  </section>

  <section class="card card--front" aria-label="Business card front">
    <svg class="swoosh" viewBox="0 0 720 411" aria-hidden="true">
      <path d="M0,0 H150 C92,120 74,260 112,411 H0 Z" fill="var(--blue)"/>
      <path d="M0,0 H60 C30,140 30,280 60,411 H0 Z" fill="var(--blue-deep)" opacity="0.35"/>
      <path d="M162,0 C104,120 88,260 128,411 H214 C150,300 150,140 206,0 Z" fill="var(--orange)"/>
    </svg>

    <div class="brand">
      <span class="brand__dot"></span>
      <span class="brand__name">KV Relay</span>
    </div>

    <div class="holder">
      <p class="holder__name">Tom Variscoff</p>
      <p class="holder__role">CEO</p>
    </div>

    <ul class="contact">
      <li>
        <svg viewBox="0 0 14 14"><circle cx="7" cy="7" r="7" fill="var(--blue)"/><path d="M7 3a2.5 2.5 0 0 0-2.5 2.5C4.5 7.5 7 11 7 11s2.5-3.5 2.5-5.5A2.5 2.5 0 0 0 7 3z" fill="#fff"/></svg>
        <span>3F B28 GALERI NUSAPARK<br>JAKARTA PUSAT 14071</span>
      </li>
      <li>
        <svg viewBox="0 0 14 14"><circle cx="7" cy="7" r="7" fill="var(--blue)"/><path d="M4.5 3.5l1.6 1.6-.8 1.1a5 5 0 0 0 2.5 2.5l1.1-.8 1.6 1.6-1 1c-2.8 0-6-3.2-6-6z" fill="#fff"/></svg>
        <span>+62 21 5550 1842</span>
      </li>
      <li>
        <svg viewBox="0 0 14 14"><circle cx="7" cy="7" r="7" fill="var(--blue)"/><rect x="5" y="3" width="4" height="8" rx="0.8" fill="#fff"/></svg>
        <span>+62 857 5550 2391</span>
      </li>
      <li>
        <svg viewBox="0 0 14 14"><circle cx="7" cy="7" r="7" fill="var(--blue)"/><rect x="3.5" y="4.5" width="7" height="5" fill="#fff"/><path d="M3.5 4.5L7 7.3l3.5-2.8" stroke="var(--blue)" stroke-width="0.8" fill="none"/></svg>
        <span>tom@kvrelay.com</span>
      </li>
      <li>
        <svg viewBox="0 0 14 14"><circle cx="7" cy="7" r="7" fill="var(--blue)"/><circle cx="7" cy="7" r="3.6" stroke="#fff" stroke-width="0.9" fill="none"/><path d="M3.4 7h7.2M7 3.4c-1.6 2-1.6 5.2 0 7.2M7 3.4c1.6 2 1.6 5.2 0 7.2" stroke="#fff" stroke-width="0.7" fill="none"/></svg>
        <span>www.kvrelay.com</span>
      </li>
    </ul>
  </section>

</main>
</body>
</html>
```